" distribuidora no ramo do atacado e varejo (loja fisica ) nos produtos de embalagens em geral (descartáveis, festas e etc.) produtos de limpezas para (residencias , comércios e industriais ) e produtos personalizados no mesmo ramo. "

```html
<!DOCTYPE html>
<html lang="pt-BR">
<head>
<meta charset="UTF-8">
<title>Varello Distribuidora – Bloco de anotações</title>
<link rel="stylesheet" href="https://fonts.googleapis.com/css2?family=Montserrat:wght@400;600;700&display=swap">
<style>
  :root {
    --bg: #e4e6e8;
    --blue: #1d6f9f;
    --blue-dark: #155a85;
    --blue-light: #2a84b6;
    --green: #6cc04a;
    --green-light: #a6dc5a;
    --white: #ffffff;
    --ring: #2f8fc4;
    --ink-blue: #1f5f8c;
    --grey: #6f7b84;
  }
  * { box-sizing: border-box; margin: 0; padding: 0; }
  html, body { width: 1200px; height: 1200px; overflow: hidden; }
  body {
    background: var(--bg);
    font-family: "Montserrat", Arial, sans-serif;
    position: relative;
  }
  .pad {
    position: absolute;
    width: 340px;
    height: 520px;
    box-shadow: 0 6px 18px rgba(0,0,0,0.18);
  }
  .pad--front { left: 90px; top: 410px; }
  .pad--page { left: 430px; top: 340px; z-index: 2; }
  .pad--back { left: 770px; top: 410px; }

  .cover {
    background: linear-gradient(160deg, var(--blue-light), var(--blue) 45%, var(--blue-dark));
    overflow: hidden;
  }
  .cover .green-band {
    position: absolute; left: 0; right: 0; bottom: 0; height: 26px;
    background: linear-gradient(90deg, var(--green), var(--green-light), var(--green));
  }
  .cover .green-band::before {
    content: ""; position: absolute; left: 0; right: 0; top: -4px; height: 4px;
    background: rgba(255,255,255,0.35);
  }
  .page { background: var(--white); }

  .binding {
    position: absolute; top: -14px; left: 18px; right: 18px; height: 30px;
  }

  .brand { position: absolute; left: 0; right: 0; text-align: center; }
  .brand__mark {
    width: 64px; height: 64px; border-radius: 50%;
    margin: 0 auto 16px;
    background: var(--green);
  }
  .brand__name {
    font-weight: 700; letter-spacing: 2px; line-height: 1;
  }
  .brand__tag {
    font-weight: 400; letter-spacing: 5px; margin-top: 6px;
  }
  .pad--front .brand { top: 170px; color: var(--white); }
  .pad--front .brand__name { font-size: 40px; }
  .pad--front .brand__tag { font-size: 11px; }

  .pad--page .brand { top: 60px; color: var(--ink-blue); }
  .pad--page .brand__mark { width: 36px; height: 36px; margin-bottom: 8px; }
  .pad--page .brand__name { font-size: 20px; }
  .pad--page .brand__tag { font-size: 6px; letter-spacing: 3px; margin-top: 3px; }

  .decor-area {
    position: absolute; left: -10px; top: 90px; width: 250px; height: 250px;
    border-radius: 50% 50% 50% 10%;
    background: radial-gradient(circle at 60% 40%, var(--green-light), var(--green) 45%, rgba(42,132,182,0.0) 75%);
    opacity: 0.9;
  }
  .back-brand {
    position: absolute; right: 22px; top: 300px; text-align: right; color: var(--white);
    display: flex; align-items: center; gap: 8px;
  }
  .back-brand__mark { width: 18px; height: 18px; border-radius: 50%; background: var(--green); }
  .back-brand__name { font-size: 16px; font-weight: 700; letter-spacing: 1px; }
  .contact {
    position: absolute; right: 22px; top: 348px; list-style: none;
    color: var(--white); font-size: 9px;
  }
  .contact li {
    display: flex; align-items: center; justify-content: flex-end;
    gap: 8px; height: 24px;
  }
  .contact svg { width: 11px; height: 11px; fill: var(--white); }
</style>
</head>
<body>

<svg width="0" height="0" style="position:absolute">
  <defs>
    <g id="ring">
      <rect x="0" y="0" width="4" height="22" rx="2" fill="var(--ring)"/>
      <circle cx="2" cy="24" r="2.6" fill="#0f3f5f"/>
    </g>
  </defs>
</svg>

<section class="pad pad--front cover">
  <svg class="binding" viewBox="0 0 304 30" preserveAspectRatio="none">
    <g>
      <use href="#ring" x="2"/><use href="#ring" x="14"/><use href="#ring" x="26"/><use href="#ring" x="38"/>
      <use href="#ring" x="50"/><use href="#ring" x="62"/><use href="#ring" x="74"/><use href="#ring" x="86"/>
      <use href="#ring" x="98"/><use href="#ring" x="110"/><use href="#ring" x="122"/><use href="#ring" x="134"/>
      <use href="#ring" x="146"/><use href="#ring" x="158"/><use href="#ring" x="170"/><use href="#ring" x="182"/>
      <use href="#ring" x="194"/><use href="#ring" x="206"/><use href="#ring" x="218"/><use href="#ring" x="230"/>
      <use href="#ring" x="242"/><use href="#ring" x="254"/><use href="#ring" x="266"/><use href="#ring" x="278"/>
      <use href="#ring" x="290"/>
    </g>
  </svg>
  <div class="brand">
    <div class="brand__mark"></div>
    <div class="brand__name">VARELLO</div>
    <div class="brand__tag">DISTRIBUIDORA</div>
  </div>
  <div class="green-band"></div>
</section>

<section class="pad pad--page page">
  <svg class="binding" viewBox="0 0 304 30" preserveAspectRatio="none">
    <g>
      <use href="#ring" x="2"/><use href="#ring" x="14"/><use href="#ring" x="26"/><use href="#ring" x="38"/>
      <use href="#ring" x="50"/><use href="#ring" x="62"/><use href="#ring" x="74"/><use href="#ring" x="86"/>
      <use href="#ring" x="98"/><use href="#ring" x="110"/><use href="#ring" x="122"/><use href="#ring" x="134"/>
      <use href="#ring" x="146"/><use href="#ring" x="158"/><use href="#ring" x="170"/><use href="#ring" x="182"/>
      <use href="#ring" x="194"/><use href="#ring" x="206"/><use href="#ring" x="218"/><use href="#ring" x="230"/>
      <use href="#ring" x="242"/><use href="#ring" x="254"/><use href="#ring" x="266"/><use href="#ring" x="278"/>
      <use href="#ring" x="290"/>
    </g>
  </svg>
  <div class="brand">
    <div class="brand__mark"></div>
    <div class="brand__name">VARELLO</div>
    <div class="brand__tag">DISTRIBUIDORA</div>
  </div>
</section>

<section class="pad pad--back cover">
  <svg class="binding" viewBox="0 0 304 30" preserveAspectRatio="none">
    <g>
      <use href="#ring" x="2"/><use href="#ring" x="14"/><use href="#ring" x="26"/><use href="#ring" x="38"/>
      <use href="#ring" x="50"/><use href="#ring" x="62"/><use href="#ring" x="74"/><use href="#ring" x="86"/>
      <use href="#ring" x="98"/><use href="#ring" x="110"/><use href="#ring" x="122"/><use href="#ring" x="134"/>
      <use href="#ring" x="146"/><use href="#ring" x="158"/><use href="#ring" x="170"/><use href="#ring" x="182"/>
      <use href="#ring" x="194"/><use href="#ring" x="206"/><use href="#ring" x="218"/><use href="#ring" x="230"/>
      <use href="#ring" x="242"/><use href="#ring" x="254"/><use href="#ring" x="266"/><use href="#ring" x="278"/>
      <use href="#ring" x="290"/>
    </g>
  </svg>
  <div class="decor-area" role="img" aria-label="Large green and blue brand-symbol decoration"></div>
  <div class="back-brand">
    <span class="back-brand__mark"></span>
    <span class="back-brand__name">VARELLO</span>
  </div>
  <ul class="contact">
    <li>contato@varello.com.br
      <svg viewBox="0 0 12 12"><rect x="1" y="2.5" width="10" height="7" rx="1"/></svg></li>
    <li>55 9999-0000
      <svg viewBox="0 0 12 12"><rect x="3" y="1" width="6" height="10" rx="1"/></svg></li>
    <li>55 99999-0000
      <svg viewBox="0 0 12 12"><rect x="3" y="1" width="6" height="10" rx="1"/></svg></li>
    <li>Rua do Projeto, 999
      <svg viewBox="0 0 12 12"><path d="M6 0.5a4 4 0 0 0-4 4c0 3 4 7 4 7s4-4 4-7a4 4 0 0 0-4-4zm0 5.6a1.6 1.6 0 1 1 0-3.2 1.6 1.6 0 0 1 0 3.2z"/></svg></li>
  </ul>
  <div class="green-band"></div>
</section>

</body>
</html>
```